Zielgruppe
Unter dem Markennamen Kestrilo vertreiben wir Produkte, welche von uns selbst entwickelt werden. Ein Bestandteil eines jeden Produktes ist dabei immer etwas aus Bambus. Die Zielgruppe ist sehr unspezifisch, aber eher junge Erwachsene und Erwachsene im mittleren Alter. Bei den Produkten handelt es sich um Haushaltsprodukte bzw. kleinere Möbelstücke. Für ein neues Schneidebrett Set wird jetzt ein schönes Verpackungsdesign gesucht.
Aufgabenstellung
Wir haben ein komplettes Briefing mit unseren Vorstellungen erstellt.

```html
<!DOCTYPE html>
<html lang="de">
<head>
<meta charset="utf-8">
<title>Kestrilo Schneidebrett Set – Verpackung</title>
<link rel="stylesheet" href="https://fonts.googleapis.com/css2?family=Open+Sans:ital,wght@0,400;0,600;0,700;1,400;1,800&display=swap">
<style>
  :root{
    --bg:#ffffff;
    --green:#3f7a37;
    --green-dark:#2f5e2a;
    --bamboo-light:#d3e3bd;
    --wood:#d6a35b;
    --wood-light:#e8c48a;
    --cut:#e2399d;
    --fold:#7bbf72;
    --text:#3a3a3a;
    --photo-red:#b8464f;
  }
  *{box-sizing:border-box;margin:0;padding:0}
  html,body{width:1200px;height:1200px;overflow:hidden;background:var(--bg)}
  body{position:relative;font-family:"Open Sans",sans-serif;color:var(--text)}
  .net{position:absolute;left:300px;top:60px;width:600px;height:1080px}
  .panel{position:absolute;border:1.5px solid var(--cut);background:#fff}
  .fold{border-color:var(--fold);border-style:dashed}
  .flap-top{left:60px;top:0;width:480px;height:70px;border-bottom:none}
  .side-flap{top:70px;width:60px;height:360px;border-radius:6px}
  .side-flap.left{left:0}.side-flap.right{left:540px}
  .back{left:60px;top:70px;width:480px;height:360px;border-left:1.5px dashed var(--fold);border-right:1.5px dashed var(--fold)}
  .strip{left:60px;top:430px;width:480px;height:70px;border-top:1.5px dashed var(--fold)}
  .lid{left:60px;top:500px;width:480px;height:420px;border-top:1.5px dashed var(--fold);border-bottom:1.5px dashed var(--fold)}
  .lid-flap{left:60px;top:920px;width:480px;height:90px;border-top:none;border-radius:0 0 30px 30px}
  .band{position:absolute;height:10px;background:var(--bamboo-light);border-radius:5px}
  .ph{position:absolute}
  .wordmark{font-family:"Open Sans",sans-serif;font-weight:400;color:var(--green);letter-spacing:2px}
  .title{font-family:"Open Sans",sans-serif;font-style:italic;font-weight:800;color:var(--green)}
  .caption{position:absolute;font-size:9px;font-style:italic;line-height:1.25;text-align:right;color:var(--text)}
  .dot{position:absolute;width:30px;height:30px;border-radius:50%;border:2px solid var(--green);background:var(--wood-light)}
  .eco{position:absolute;display:flex;align-items:center;gap:6px;font-weight:700;color:var(--green)}
  .eco i{display:block;width:14px;height:14px;background:var(--green)}
</style>
</head>
<body>
<div class="net">
  <div class="panel flap-top"></div>
  <div class="panel side-flap left"></div>
  <div class="panel side-flap right"></div>

  <section class="panel back">
    <div class="band" style="left:14px;top:12px;width:452px"></div>
    <div class="eco" style="left:20px;top:48px;font-size:12px"><i></i>aus Bambus</div>
    <div class="title" style="position:absolute;left:20px;top:74px;font-size:24px">Schneidebrett Set</div>
    <p style="position:absolute;left:20px;top:110px;width:230px;font-size:9px;font-style:italic;line-height:1.35">Lorem ipsum dolor sit amet, consectetuer adipiscing elit, sed diam nonummy nibh euismod tincidunt ut laoreet dolore magna aliquam erat volutpat.</p>
    <div class="ph" role="img" aria-label="Foto: Gemüse wird auf dem Bambusbrett geschnitten, Auffangschalen daneben" style="left:270px;top:48px;width:196px;height:80px;border-radius:40px 8px 8px 40px;border:3px solid var(--green);background:linear-gradient(90deg,var(--photo-red),var(--wood-light) 45%,#8fb36a)"></div>
    <div class="caption" style="left:290px;top:134px;width:176px">Dank kantenlosem Design einfach die eigene Auffangschale neben das Schneidebrett stellen.</div>
    <div class="ph" role="img" aria-label="Illustration: Schneidebrett mit ausziehbaren Brettern aus der Schublade" style="left:200px;top:180px;width:200px;height:140px;border-radius:6px;background:linear-gradient(160deg,var(--wood-light),var(--wood))"></div>
    <div class="caption" style="left:20px;top:196px;width:130px">Sicherer Stand dank Anti-Rutsch Füße</div>
    <div class="dot" style="left:158px;top:192px"></div>
    <div class="caption" style="left:20px;top:240px;width:130px">Platzsparend aufbewahren dank Standfuß</div>
    <div class="dot" style="left:158px;top:240px"></div>
    <div class="caption" style="left:20px;top:288px;width:130px">Gewünschtes Schneidebrett aus der Schublade ziehen und oben auflegen.</div>
    <div class="dot" style="left:158px;top:290px"></div>
    <div class="wordmark" style="position:absolute;right:20px;bottom:14px;font-size:22px">KESTRILO</div>
  </section>

  <section class="panel strip">
    <div class="band" style="left:14px;top:30px;width:150px"></div>
    <div class="wordmark" style="position:absolute;left:180px;top:14px;font-size:22px">KESTRILO</div>
    <div class="title" style="position:absolute;left:260px;top:44px;font-size:10px">Schneidebrett Set</div>
    <div class="band" style="left:340px;top:30px;width:126px"></div>
  </section>

  <section class="panel lid">
    <div class="title" style="position:absolute;left:24px;top:18px;font-size:20px">Schneidebrett Set</div>
    <div class="ph" role="img" aria-label="Foto: Standfuß aus Bambus" style="left:30px;top:56px;width:36px;height:28px;border-radius:4px;background:var(--wood)"></div>
    <div style="position:absolute;left:76px;top:56px;font-size:10px;font-weight:700;color:var(--green);line-height:1.2">Mit<br>Standfuß</div>
    <div class="ph" role="img" aria-label="Foto: Schneidebrett Set aus Bambus, Seitenansicht" style="left:230px;top:16px;width:230px;height:90px;border-radius:6px;background:linear-gradient(170deg,var(--wood-light),var(--wood))"></div>
    <div class="wordmark" style="position:absolute;left:0;width:480px;top:130px;text-align:center;font-size:58px;letter-spacing:4px">KESTRILO</div>
    <div class="ph" role="img" aria-label="Foto: großes Bambus-Schneidebrett mit Schubladen" style="left:0;top:220px;width:330px;height:190px;background:linear-gradient(160deg,var(--wood-light),var(--wood) 70%,#b9843f)"></div>
    <div class="eco" style="left:350px;top:320px;font-size:12px"><i></i>aus Bambus</div>
  </section>

  <section class="panel lid-flap">
    <div class="wordmark" style="position:absolute;left:210px;top:12px;font-size:18px">KESTRILO</div>
    <div class="title" style="position:absolute;left:272px;top:38px;font-size:9px">Schneidebrett Set</div>
    <div class="band" style="left:380px;top:22px;width:86px"></div>
    <div style="position:absolute;left:24px;top:60px;font-size:7px;color:#777">Made for home kitchens, crafted from bamboo</div>
  </section>

  <div style="position:absolute;left:18px;top:250px;transform:rotate(-90deg);transform-origin:left top;font-size:11px;font-weight:700;color:var(--green);white-space:nowrap">www.kestrilo.de</div>
</div>
</body>
</html>
```